Logo, homepage, and product page design cleaning equipment

Looking for a logo, homepage, and product page design for our shopify store. We sell cleaning equipment that serves the auto detailing industry. I have attached a picture of our main product. The company is called Brisk Cleaning Equipment with a slogan of The Way to Clean (slogan incorporated is optional). A site I really like is https://www.ravenmoorbrew.example/. It has a very clean layout and very clear on their messaging.

Target Market(s)

Auto detailing industry

Industry/Entity Type

Automotive

Logo Text

Brisk Cleaning Equipment

Font styles to use
Serif
Sans Serif

Requirements
Must have
• A nice clean layout. Not too busy. Easy to navigate.
Nice to have
• consistency in colors. Appeal to people who care about their cars. They have an eye for detail.
Should not have
• It cannot be too busy.

```html
<!DOCTYPE html>
<html lang="en">
<head>
<meta charset="utf-8">
<title>Brisk Cleaning Equipment — The Way to Clean</title>
<link rel="stylesheet" href="https://fonts.googleapis.com/css2?family=Alfa+Slab+One&family=Montserrat:wght@400;500;600;700&family=Questrial&display=swap">
<style>
:root{
  --red:#e8363a;
  --ink:#111111;
  --text:#333333;
  --muted:#777777;
  --rule:#c9c9c9;
  --card-border:#ececec;
  --footer:#232323;
  --footer-bottom:#1a1a1a;
  --input:#8a8a8a;
  --white:#ffffff;
}
*{margin:0;padding:0;box-sizing:border-box}
html,body{width:1200px;height:2874px;overflow:hidden;background:var(--white)}
body{position:relative;font-family:"Montserrat",sans-serif;color:var(--text)}

/* header */
.nav-link{position:absolute;top:82px;font-size:12px;font-weight:500;letter-spacing:1px;color:var(--ink);text-transform:uppercase}
.brand{position:absolute;left:520px;top:40px;width:160px;display:flex;flex-direction:column;align-items:center;gap:6px}
.brand-dot{width:34px;height:34px;border-radius:50%;background:var(--ink)}
.brand-name{font-size:10px;font-weight:700;line-height:1.3;color:var(--ink);text-transform:uppercase;letter-spacing:.5px;text-align:center}
.account{position:absolute;top:22px;left:838px;display:flex;align-items:center;gap:8px;font-size:12px;color:var(--text)}
.icon{position:absolute}

/* hero */
.product-shot{position:absolute;left:330px;top:160px;width:300px;height:430px;border-radius:40px;background:radial-gradient(ellipse at 50% 55%,#3a3a3a 0%,#1b1b1b 42%,#ffffff 70%)}
.tagline-small{position:absolute;left:702px;top:226px;font-family:"Questrial",sans-serif;font-size:32px;color:var(--ink)}
.tagline-big{position:absolute;left:700px;top:258px;width:316px;font-family:"Alfa Slab One",serif;font-size:74px;line-height:1;letter-spacing:2px;color:var(--red);white-space:nowrap}
.hero-lead{position:absolute;left:712px;top:356px;width:290px;text-align:center;font-size:14px;line-height:23px;color:var(--text)}
.price{position:absolute;left:702px;top:447px;width:306px;text-align:center;font-size:29px;font-weight:700;color:var(--ink)}
.btn{position:absolute;display:flex;align-items:center;justify-content:center;background:var(--red);color:var(--white);font-weight:500}
.btn-buy{left:702px;top:520px;width:306px;height:48px;font-size:15px}
.features{position:absolute;left:716px;top:592px;width:300px;list-style:none}
.features li{position:relative;padding-left:22px;font-size:13px;line-height:19px;margin-bottom:13px;color:var(--text)}
.features li::before{content:"";position:absolute;left:0;top:6px;width:6px;height:6px;background:var(--red)}
.warning{position:absolute;left:199px;top:641px;font-size:16px;color:var(--red);text-transform:uppercase}
.spec-title{position:absolute;left:199px;top:690px;font-size:28px;font-weight:700;color:var(--ink);letter-spacing:.5px}
.spec-lines{position:absolute;left:199px;top:734px;font-family:"Questrial",sans-serif;font-size:30px;line-height:41.5px;color:var(--ink);letter-spacing:1px}
.divider{position:absolute;left:172px;top:964px;width:856px;height:3px;background:var(--rule)}

/* sections */
.section-title{position:absolute;left:0;width:1200px;text-align:center;font-size:28px;font-weight:700;color:var(--red);letter-spacing:1px}
.photo{position:absolute}
.post-title{position:absolute;text-align:center;font-size:22px;font-weight:700;color:var(--ink)}
.post-meta{position:absolute;display:flex;justify-content:center;align-items:center;gap:18px;font-size:13px;color:var(--muted)}
.post-meta span{display:flex;align-items:center;gap:6px}

.card{position:absolute;top:2144px;height:288px;border:2px solid var(--card-border);background:var(--white)}
.card-shot{position:absolute;left:50%;top:50px;width:120px;height:190px;margin-left:-60px;border-radius:20px;background:radial-gradient(ellipse at 50% 55%,#333 0%,#161616 48%,#ffffff 72%)}
.card-name{position:absolute;top:2456px;width:416px;text-align:center;font-size:21px;font-weight:500;color:var(--ink)}
.btn-small{top:2503px;width:113px;height:34px;font-size:15px}
.arrow{position:absolute;top:2271px;width:32px;height:32px;background:var(--ink);display:flex;align-items:center;justify-content:center}

/* footer */
.footer{position:absolute;left:0;top:2584px;width:1200px;height:242px;background:var(--footer)}
.footer-bottom{position:absolute;left:0;top:2826px;width:1200px;height:48px;background:var(--footer-bottom)}
.foot-link{position:absolute;font-size:12px;font-weight:600;color:var(--white)}
.social{position:absolute;top:2782px;width:16px;height:16px;border-radius:50%;background:var(--white)}
.news-title{position:absolute;left:539px;top:2636px;font-size:18px;font-weight:700;letter-spacing:3px;color:var(--white)}
.news-text{position:absolute;left:539px;top:2678px;font-size:13px;font-weight:500;color:var(--white)}
.news-input{position:absolute;left:539px;top:2711px;width:342px;height:34px;background:var(--input);color:#d8d8d8;font-size:12px;padding:11px 14px}
.news-btn{left:539px;top:2750px;width:342px;height:34px;font-size:15px;font-weight:600}
.copyright{position:absolute;left:249px;top:2840px;font-size:12px;color:var(--white)}
</style>
</head>
<body>

<header>
  <a class="nav-link" style="left:373px">About</a>
  <a class="nav-link" style="left:460px">Shop</a>
  <div class="brand"><span class="brand-dot"></span><span class="brand-name">Brisk Cleaning Equipment</span></div>
  <a class="nav-link" style="left:707px">Blog</a>
  <a class="nav-link" style="left:784px">Contact Us</a>
  <div class="account">
    <svg width="14" height="14" viewBox="0 0 14 14"><circle cx="7" cy="4" r="3.2" fill="#555"/><path d="M1 14c0-4 3-6 6-6s6 2 6 6z" fill="#555"/></svg>
    Login / Sign up
  </div>
  <svg class="icon" style="left:963px;top:22px" width="16" height="16" viewBox="0 0 16 16"><circle cx="6.5" cy="6.5" r="4.5" stroke="#555" stroke-width="2" fill="none"/><path d="M10 10l4.5 4.5" stroke="#555" stroke-width="2"/></svg>
  <svg class="icon" style="left:992px;top:14px" width="26" height="24" viewBox="0 0 26 24"><path d="M1 10h3l2.5 9h10l2.5-7H6" stroke="#555" stroke-width="2" fill="none"/><circle cx="8" cy="22" r="1.5" fill="#555"/><circle cx="15" cy="22" r="1.5" fill="#555"/><circle cx="20" cy="5" r="4.5" fill="var(--red)"/></svg>
</header>

<main>
  <section class="hero">
    <div class="product-shot" role="img" aria-label="Black pump-action foam sprayer bottle with blue trigger on white"></div>
    <div class="tagline-small">The Way to</div>
    <div class="tagline-big">CLEAN</div>
    <p class="hero-lead">Excepteur sint occaecat cupidatat non proident sunt in culpa qui officia deserunt mollit anim</p>
    <div class="price">$25.99</div>
    <a class="btn btn-buy">Buy Now</a>
    <ul class="features">
      <li>Nemo enim ipsam voluptatem quia sit aspernatur aut odit aut fugit</li>
      <li>Sed quia consequuntur magni dolores eos qui ratione voluptatem sequi</li>
      <li>Quis nostrum exercitationem ullam corporis suscipit laboriosam</li>
      <li>Quis autem vel eum iure qui in ea voluptate velit esse quam</li>
      <li>Vel illum qui dolorem eum fugiat quo voluptas nulla pariatur</li>
      <li>Qui officia deserunt mollitia animi id est laborum et dolorum fuga</li>
    </ul>
    <div class="warning">Warning : Similique sunt in culpa</div>
    <div class="spec-title">OFFICIA DESERUNT MOLLITIA</div>
    <div class="spec-lines">QUO MINUS ID QUOD MAXIME<br>PLACEAT FACERE POSSIMUS<br>RERUMREICIENDIS<br>MAIORES ALIAS</div>
  </section>

  <div class="divider"></div>

  <section class="blog">
    <h2 class="section-title" style="top:1016px">OUR BLOG</h2>
    <div class="photo" style="left:172px;top:1102px;width:856px;height:383px;background:linear-gradient(135deg,#2a3550 0%,#1b2238 40%,#5a6a88 70%,#c8d23a 100%)" role="img" aria-label="Dark blue car covered in soap foam being washed with a wash mitt"></div>
    <div class="post-title" style="left:172px;top:1518px;width:856px">Nam libero tempore cum soluta nobis est eligendi</div>
    <div class="post-meta" style="left:172px;top:1568px;width:856px">
      <span><svg width="11" height="11" viewBox="0 0 14 14"><circle cx="7" cy="4" r="3.2" fill="#777"/><path d="M1 14c0-4 3-6 6-6s6 2 6 6z" fill="#777"/></svg>Admin</span>
      <span><svg width="11" height="11" viewBox="0 0 12 12"><rect x="1" y="2" width="10" height="9" fill="none" stroke="#777" stroke-width="1.5"/><path d="M1 5h10" stroke="#777" stroke-width="1.5"/></svg>12th Sept 2018</span>
    </div>

    <div class="photo" style="left:172px;top:1621px;width:415px;height:235px;background:linear-gradient(135deg,#151515 0%,#2b2b2b 55%,#7ec8d8 80%,#9acd32 100%)" role="img" aria-label="Hands spraying and wiping the bonnet of a black car"></div>
    <div class="post-title" style="left:172px;top:1891px;width:415px">Nam libero tempore cum soluta</div>
    <div class="post-meta" style="left:172px;top:1938px;width:415px">
      <span><svg width="11" height="11" viewBox="0 0 14 14"><circle cx="7" cy="4" r="3.2" fill="#777"/><path d="M1 14c0-4 3-6 6-6s6 2 6 6z" fill="#777"/></svg>Admin</span>
      <span><svg width="11" height="11" viewBox="0 0 12 12"><rect x="1" y="2" width="10" height="9" fill="none" stroke="#777" stroke-width="1.5"/><path d="M1 5h10" stroke="#777" stroke-width="1.5"/></svg>12th Sept 2018</span>
    </div>

    <div class="photo" style="left:611px;top:1621px;width:417px;height:235px;background:linear-gradient(160deg,#7a2a22 0%,#3a3a3a 45%,#8a8a8a 75%,#5a5048 100%)" role="img" aria-label="Person washing a foam-covered dark car in a driveway"></div>
    <div class="post-title" style="left:611px;top:1891px;width:417px">Quod maxime placeat facere</div>
    <div class="post-meta" style="left:611px;top:1938px;width:417px">
      <span><svg width="11" height="11" viewBox="0 0 14 14"><circle cx="7" cy="4" r="3.2" fill="#777"/><path d="M1 14c0-4 3-6 6-6s6 2 6 6z" fill="#777"/></svg>Admin</span>
      <span><svg width="11" height="11" viewBox="0 0 12 12"><rect x="1" y="2" width="10" height="9" fill="none" stroke="#777" stroke-width="1.5"/><path d="M1 5h10" stroke="#777" stroke-width="1.5"/></svg>12th Sept 2018</span>
    </div>
  </section>

  <section class="products">
    <h2 class="section-title" style="top:2060px">OTHER PRODUCTS</h2>
    <div class="arrow" style="left:106px"><svg width="12" height="12" viewBox="0 0 12 12"><path d="M8 1L3 6l5 5" stroke="#fff" stroke-width="2.5" fill="none"/></svg></div>
    <div class="card" style="left:172px;width:416px"><div class="card-shot" role="img" aria-label="Black foam sprayer bottle"></div></div>
    <div class="card" style="left:612px;width:416px"><div class="card-shot" role="img" aria-label="Black foam sprayer bottle"></div></div>
    <div class="arrow" style="left:1052px"><svg width="12" height="12" viewBox="0 0 12 12"><path d="M4 1l5 5-5 5" stroke="#fff" stroke-width="2.5" fill="none"/></svg></div>
    <div class="card-name" style="left:172px">Dolorem eum fugiat quo</div>
    <div class="card-name" style="left:612px">Dolorem eum fugiat quo</div>
    <a class="btn btn-small" style="left:323px">Buy Now</a>
    <a class="btn btn-small" style="left:763px">Buy Now</a>
  </section>
</main>

<footer>
  <div class="footer"></div>
  <a class="foot-link" style="left:242px;top:2654px">About</a>
  <a class="foot-link" style="left:242px;top:2679px">Shop</a>
  <a class="foot-link" style="left:242px;top:2704px">Blog</a>
  <a class="foot-link" style="left:242px;top:2729px">Contact Us</a>
  <a class="foot-link" style="left:319px;top:2654px">Terms and Conditions</a>
  <a class="foot-link" style="left:319px;top:2679px">Shipping Details</a>
  <span class="social" style="left:257px"></span>
  <span class="social" style="left:288px"></span>
  <span class="social" style="left:324px"></span>
  <div class="news-title">NEWSLETTER</div>
  <div class="news-text">Subscribe to our newsletter for latest updates</div>
  <div class="news-input">Email</div>
  <a class="btn news-btn">Subscribe</a>
  <div class="footer-bottom"></div>
  <div class="copyright">©Copyright information here</div>
</footer>

</body>
</html>
```